VORELT B2B portal design
Fantastic design work, top communication and fast design changes! Many thanks,Jens & Uwe from VORELT
Zielgruppe
We are a B2B Cloud Services StartUp that creates B2B logistics & supply chain processes between customer and its suppliers.
Aufgabenstellung
We need a modern responsive able design, that should consider that we are NOT presenting goods or clothes or similar on the portal pages but we show mainly data grids, kpi dashboards, forms, and setting panels to our customer and their suppliers.
The design must be clean and straight not to distract people from the important information in these data grids, kpi dashboards, forms, and settings panels.
We need our logo perfectly embedded and the pages coloured around from grey to blue.
The Designer must be able to deliver a design and transfer it to a highly responsive HTML (5) template (without technical content or further functionality). This our programmers will implement afterwards in .Net.
We need in total 3 page templates:
1. Login Page
2. Main Page with overview over the following services text (each one shown in one tile)
"ZMS (Time Frame Management)"
"DMS (Document Management)"
"REMS (Reporting Management)"
-> Note: At the end we will have up to 12 or more tiles (services) so the design should be additive
3. Data grid (e.g. list of customers)/form (e.g. customer registration form) page to show some data grid with database data
See samples for each page enclosed!!

```html
<!DOCTYPE html>
<html lang="en">
<head>
<meta charset="utf-8">
<title>VORELT – User Registration</title>
<link rel="stylesheet" href="https://fonts.googleapis.com/css2?family=Ubuntu:wght@500;700&family=Ubuntu+Condensed&family=Open+Sans:wght@400;600&display=swap">
<style>
:root{
  --navy:#062a47;
  --navy-text:#0d2c48;
  --sidebar:#e3e7ea;
  --sidebar-line:#cfd5da;
  --page:#f3f4f5;
  --card:#ffffff;
  --label:#4a4a4a;
  --placeholder:#a9a9a9;
  --input-border:#c3c6c9;
  --focus-border:#2e5a80;
  --ok-bg:#e4f3d9;
  --ok-border:#79c24a;
  --ok-text:#3c8a1a;
  --err-bg:#f4ded8;
  --err-border:#d9683f;
  --err-text:#8a2a12;
  --link-red:#e0201b;
}
*{box-sizing:border-box;margin:0;padding:0}
html,body{width:1200px;height:904px;overflow:hidden}
body{position:relative;background:var(--page);font-family:"Open Sans",sans-serif;color:var(--label)}

.topbar{position:absolute;left:0;top:0;width:1200px;height:72px;background:var(--navy);color:#fff}
.user{position:absolute;right:110px;top:16px;text-align:right}
.user-name{font-family:"Ubuntu",sans-serif;font-weight:700;font-size:19px;line-height:22px}
.user-mail{font-family:"Ubuntu",sans-serif;font-weight:500;font-size:13px;line-height:16px;margin-top:2px}
.avatar{position:absolute;left:1106px;top:10px;width:52px;height:52px;border-radius:50%;background:radial-gradient(circle at 50% 40%,#8a8580,#3b3835);border:2px solid #d0d0d0}
.caret{position:absolute;left:1172px;top:31px}

.sidebar{position:absolute;left:0;top:72px;width:329px;height:770px;background:var(--sidebar);border-right:1px solid #d7dbde}
.brand{height:220px;background:linear-gradient(135deg,#d3d7da 0%,#eef0f1 45%,#dde1e4 70%,#e8eaec 100%);display:flex;align-items:center;justify-content:center;gap:14px}
.brand-dot{width:22px;height:22px;border-radius:50%;background:var(--navy)}
.brand-name{font-family:"Ubuntu Condensed",sans-serif;font-size:64px;color:var(--navy);letter-spacing:2px}
.nav{list-style:none}
.nav-item{height:61px;display:flex;align-items:center;padding-left:22px;gap:10px;font-family:"Ubuntu Condensed",sans-serif;font-size:20px;color:var(--navy-text);border-top:1px solid var(--sidebar-line)}
.nav-item svg{width:26px;height:22px;flex:none}
.nav-item.is-active{background:var(--navy);color:#fff}

.page-title{position:absolute;left:370px;top:140px;font-family:"Ubuntu Condensed",sans-serif;font-size:27px;color:#3b3f44;letter-spacing:.3px}
.card{position:absolute;left:368px;top:196px;width:807px;height:602px;background:var(--card);box-shadow:0 2px 2px rgba(0,0,0,.12)}
.card-intro{position:absolute;left:0;top:46px;width:100%;text-align:center;font-family:"Ubuntu Condensed",sans-serif;font-size:18px;color:#2b2f33}
.alert{position:absolute;top:110px;width:365px;height:40px;border:1px solid;border-radius:2px;padding-left:14px;font-size:14px;line-height:38px}
.alert-success{left:28px;background:var(--ok-bg);border-color:var(--ok-border);color:var(--ok-text)}
.alert-error{left:424px;background:var(--err-bg);border-color:var(--err-border);color:var(--err-text)}
.field{position:absolute;width:259px}
.field-label{display:block;font-size:14px;color:var(--label);margin-bottom:8px;padding-left:2px}
.field-input{height:42px;border:1px solid var(--input-border);border-radius:4px;padding-left:14px;font-size:14px;line-height:40px;color:var(--placeholder);background:#fff}
.field-input.is-focus{border-color:var(--focus-border);color:#333}
.field-input.is-secret{letter-spacing:3px;font-size:12px}
.check{position:absolute;left:32px;display:flex;align-items:center;gap:10px;font-size:14px;color:#555}
.check-box{width:19px;height:19px;border-radius:3px;background:#e0e3e6;display:flex;align-items:center;justify-content:center}
.terms{color:var(--link-red)}
.btn-register{position:absolute;left:34px;top:495px;width:118px;height:41px;background:var(--navy);color:#fff;border:0;border-radius:2px;font-family:"Open Sans",sans-serif;font-size:14px;font-weight:600}

.footer{position:absolute;left:0;top:842px;width:1200px;height:62px;background:#fff;border-top:1px solid #e4e6e8;font-family:"Ubuntu Condensed",sans-serif;font-size:16px;color:#2b2f33}
.footer-copy{position:absolute;left:14px;top:22px}
.footer-links{position:absolute;right:22px;top:22px;word-spacing:3px}
</style>
</head>
<body>
<header class="topbar">
  <div class="user">
    <div class="user-name">Lena Marsh</div>
    <div class="user-mail">lena_marsh@vorelt-mail.com</div>
  </div>
  <div class="avatar" role="img" aria-label="User profile photo"></div>
  <svg class="caret" width="10" height="8" viewBox="0 0 10 8"><path d="M0 0h10L5 7z" fill="#fff"/></svg>
</header>

<aside class="sidebar">
  <div class="brand"><span class="brand-dot"></span><span class="brand-name">VORELT</span></div>
  <ul class="nav">
    <li class="nav-item"><svg viewBox="0 0 26 22"><circle cx="13" cy="11" r="9" fill="none" stroke="#0d2c48" stroke-width="2"/><rect x="3" y="8" width="20" height="6" fill="#0d2c48"/></svg>My News</li>
    <li class="nav-item"><svg viewBox="0 0 26 22"><circle cx="9" cy="6" r="5" fill="#0d2c48"/><path d="M0 21c0-7 4-9 9-9s7 2 7 5v4z" fill="#0d2c48"/><circle cx="20" cy="17" r="4" fill="none" stroke="#0d2c48" stroke-width="2.4"/></svg>My User Settings</li>
    <li class="nav-item is-active"><svg viewBox="0 0 26 22"><circle cx="9" cy="12" r="6" fill="none" stroke="#fff" stroke-width="4" stroke-dasharray="3 2"/><circle cx="20" cy="6" r="3.5" fill="none" stroke="#fff" stroke-width="3" stroke-dasharray="2 1.5"/><circle cx="20" cy="17" r="3" fill="none" stroke="#fff" stroke-width="2.5" stroke-dasharray="2 1.5"/></svg>Company Settings</li>
    <li class="nav-item"><svg viewBox="0 0 26 22"><path d="M4 20L16 8M18 2l4 4-4 4-4-4z" stroke="#0d2c48" stroke-width="3" fill="none"/><path d="M5 3l15 16" stroke="#0d2c48" stroke-width="3"/></svg>Configuration</li>
    <li class="nav-item"><svg viewBox="0 0 26 22"><g fill="#0d2c48"><rect x="2" y="2" width="5" height="4"/><rect x="9" y="2" width="15" height="4"/><rect x="2" y="9" width="5" height="4"/><rect x="9" y="9" width="15" height="4"/><rect x="2" y="16" width="5" height="4"/><rect x="9" y="16" width="15" height="4"/></g></svg>Services</li>
    <li class="nav-item"><svg viewBox="0 0 26 22"><ellipse cx="13" cy="10" rx="10" ry="7" fill="#0d2c48"/><path d="M5 14l-2 6 7-4z" fill="#0d2c48"/></svg>Communication</li>
    <li class="nav-item"><svg viewBox="0 0 26 22"><path d="M12 4H4v15h15v-8" fill="none" stroke="#0d2c48" stroke-width="2.5"/><path d="M10 13L21 2M15 2h6v6" fill="none" stroke="#0d2c48" stroke-width="2.5"/></svg>Logout</li>
  </ul>
</aside>

<main>
  <h1 class="page-title">USER REGISTRATION FORM</h1>
  <section class="card">
    <p class="card-intro">Please type your account info here.</p>
    <div class="alert alert-success">Success messae</div>
    <div class="alert alert-error">Error messae</div>

    <div class="field" style="left:28px;top:192px"><span class="field-label">Username:</span><div class="field-input is-focus">John</div></div>
    <div class="field" style="left:388px;top:192px"><span class="field-label">Password:</span><div class="field-input is-secret">•••••••</div></div>
    <div class="field" style="left:28px;top:305px"><span class="field-label">Mail:</span><div class="field-input">Type your mail here</div></div>
    <div class="field" style="left:388px;top:305px"><span class="field-label">Phone:</span><div class="field-input">Type your phone here</div></div>

    <div class="check" style="top:406px"><span class="check-box"><svg width="11" height="8" viewBox="0 0 11 8"><path d="M1 3l3.5 3.5L10 1" fill="none" stroke="#555" stroke-width="1.5"/></svg></span>I Agree with <span class="terms">Terms Of Use</span></div>
    <div class="check" style="top:442px"><span class="check-box"><svg width="11" height="8" viewBox="0 0 11 8"><path d="M1 3l3.5 3.5L10 1" fill="none" stroke="#555" stroke-width="1.5"/></svg></span>Remember me</div>

    <button class="btn-register" type="button">REGISTER</button>
  </section>
</main>

<footer class="footer">
  <span class="footer-copy">© 2016 VORELT. All rights reserved.</span>
  <span class="footer-links">Help / Disclaimer / Contact</span>
</footer>
</body>
</html>
```